Cover for a Series of 5 Poetry Books where there is only a subtle (colour?) change for each

I have 5 poetry books to publish all have the main title of Harbours Beneath Quiet Skies then have different subtitles, which are Drifting Alone Past Amber Straits; Drifting Alone Past Ember Bays, and 3 others I have yet to determine. I have already published the first one and will attach the cover, which needs re-doing for a reprint. I have been given permission to use a photograph of the moon and a universe star pic as I like the idea of using the moon, as it dominates the tides, oceans and weather systems. I like the thought of using the stars because I love to watch them out at sea and the first design of the book I really love, except that I don't have it in 30dpi which is a must. the photo of the boat on the front is a photo of my boat, and I would like to use it too if possible. all that said I am up for some new ideas that you come up with. my poetry is pretty raw at times, but can also be inspiring and I think the book cover needs to reflect this. I am a solo sailor so it has to reflect that too!
I would like the series of 5 books to have covers that are easily recognisable as a series but also are such that people want to pick them up and read. Maybe change the colour of the moon?
I will have a series of 5 books in paperback and e-books printed 6'x9' with approx 116 to 130 pages max I have the back cover info, the photo of the boat and photo of the author. I can get the barcode for the ISBN numbers. I am self-publishing so I do not have a heap of money!
I have had a couple of folk who have kindly reproduced what I already had, that is not what I am looking for. If I am still not clear, please do drop me a line. I am very new to this process.
Thanks
Target Market(s)
Male and female 15 to 35 and 65 to 85
Requirements
Must have
- 5 covers which are clearly slightly different, but recognisable as a series
Should not have
- unhelpful comments - thanks

```html
<!DOCTYPE html>
<html lang="en">
<head>
<meta charset="utf-8">
<title>Harbours Beneath Quiet Skies – Cover Series</title>
<link rel="stylesheet" href="https://fonts.googleapis.com/css2?family=Allison&family=Open+Sans:wght@300;400;700&display=swap">
<style>
  :root {
    --stage-top: #eef0f2;
    --stage-mid: #f7f8f9;
    --paper: #ffffff;
    --label: #111111;
    --ink-light: #f2f2f4;
    --ink-sub: #8690b8;
    --sky-navy: #2b2c55;
    --sky-deep: #1a1b2c;
    --sky-dusk: #2a1f22;
    --sky-slate: #1c1c24;
    --sea-blue: #2a3596;
    --sea-dark: #141732;
    --moon-light: #dedcc2;
    --moon-mid: #bdbb9f;
    --moon-shade: #8e8c76;
    --moon-glow: rgba(214, 184, 120, 0.55);
    --portrait: #9a8a80;
    --code-box: #ffffff;
  }
  * { margin: 0; padding: 0; box-sizing: border-box; }
  html, body { width: 1143px; height: 1200px; overflow: hidden; background: var(--paper); }
  body { position: relative; font-family: "Open Sans", Arial, sans-serif; }

  .stage {
    position: absolute; left: 0; top: 0; width: 1143px; height: 777px;
    background: radial-gradient(ellipse at 50% 45%, var(--stage-mid) 0%, var(--stage-top) 100%);
  }
  .sheet { position: absolute; left: 0; top: 777px; width: 1143px; height: 423px; background: var(--paper); }

  .label {
    position: absolute; font-size: 23px; line-height: 30px; font-weight: 400;
    color: var(--label); letter-spacing: 0.2px;
  }
  .label--back { left: 50px; top: 808px; }
  .label--extra { left: 461px; top: 808px; width: 190px; }

  /* Cover component — 1em equals 1% of cover width */
  .cover {
    position: absolute; overflow: hidden;
    width: var(--w); height: calc(var(--w) * 1.5);
    font-size: calc(var(--w) / 100);
  }
  .cover__scene {
    position: absolute; inset: 0;
    background:
      linear-gradient(180deg, transparent 0%, transparent 74%, rgba(42,53,150,0.85) 82%, rgba(34,44,130,0.7) 90%, var(--sea-dark) 100%),
      linear-gradient(180deg, var(--top) 0%, var(--sky-deep) 55%, #161830 72%);
  }
  .cover--navy { --top: var(--sky-navy); }
  .cover--dusk { --top: var(--sky-dusk); }
  .cover--slate { --top: var(--sky-slate); }

  .cover__author {
    position: absolute; left: 12%; top: 9%;
    font-size: 4.2em; font-weight: 400; color: var(--ink-light);
  }
  .cover__title {
    position: absolute; left: 10%; top: 14%;
    font-family: "Allison", cursive; font-weight: 400;
    font-size: 15em; line-height: 1.1; color: var(--ink-light);
  }
  .cover__title span { display: block; }
  .cover__moon {
    position: absolute; border-radius: 50%;
    left: 55%; top: 17%; width: 66em; height: 66em;
    background: radial-gradient(circle at 45% 40%, var(--moon-light) 0%, var(--moon-mid) 60%, var(--moon-shade) 100%);
    box-shadow: 0 0 3em 1em var(--moon-glow);
  }
  .cover__subtitle {
    position: absolute; left: 12%; right: 0; top: 83%;
    display: flex; justify-content: space-between;
    font-size: 4em; font-weight: 300; color: var(--ink-sub);
    white-space: nowrap;
  }
  .cover__subtitle span:nth-child(even) { transform: translateY(0.5em); }

  /* Large flat front */
  .cover--hero .cover__author { left: 9%; top: 8%; font-size: 5em; }
  .cover--hero .cover__title { left: 9%; top: 14%; font-size: 14em; }
  .cover--hero .cover__moon { left: 48%; top: 17%; width: 48em; height: 48em; }
  .cover--hero .cover__subtitle { left: 8%; right: 4%; top: 76%; font-size: 4.3em; }
  .cover--hero .cover__subtitle span:nth-child(2) { transform: translateY(0.6em); }
  .cover--hero .cover__subtitle span:nth-child(3) { transform: translateY(1.2em); }
  .cover--hero .cover__subtitle span:nth-child(4) { transform: translateY(1.8em); }
  .cover--hero .cover__subtitle span:nth-child(5) { transform: translateY(2.4em); }
  .cover--hero .cover__subtitle span:nth-child(6) { transform: translateY(3em); }

  /* Back cover */
  .back__heading {
    position: absolute; left: 12%; top: 17.5%;
    font-size: 2.4em; font-weight: 700; color: var(--ink-light);
  }
  .back__body {
    position: absolute; left: 12%; top: 21%; width: 80%;
    font-size: 2.1em; line-height: 1.35; color: var(--ink-light);
  }
  .back__body p { margin-bottom: 1em; }
  .back__body p.narrow { width: 54%; }
  .back__portrait {
    position: absolute; left: 56%; top: 15%; width: 37%; height: 24.7%;
    border-radius: 50%; background: radial-gradient(circle at 50% 45%, #c8b5a6 0%, var(--portrait) 70%, #6d6460 100%);
  }
  .back__code-area {
    position: absolute; left: 59.5%; top: 81.6%; width: 33%; height: 12.2%;
    background: var(--code-box);
  }
  .cover--back-hero .back__heading { left: 14%; top: 16%; font-size: 3em; }
  .cover--back-hero .back__body { left: 14%; top: 21%; width: 82%; font-size: 2.7em; }
  .cover--back-hero .back__body p { width: 100%; }
</style>
</head>
<body>

<section class="stage">
  <!-- Flat back cover, large -->
  <div class="cover cover--navy cover--back-hero" style="--w:320px; left:235px; top:150px;">
    <div class="cover__scene" role="img" aria-label="Night sky fading into a dark blue sea"></div>
    <h3 class="back__heading">About the author</h3>
    <div class="back__body">
      <p>Maren has spent most of her adult life at sea, sailing small boats alone across open water. She writes at night by lantern light, keeping notes on weather, tide and memory, and shaping them later into the poems gathered here.</p>
      <p>Her work moves between fear and wonder, between long calms and sudden squalls. It is honest, sometimes raw, and always rooted in the quiet discipline of keeping watch through the dark hours until the first grey light.</p>
      <p>This is the second book in a series of five collections written over many passages. Each one follows a different stretch of water and a different season of the heart, yet all share the same moon, the same stars and the same small boat.</p>
    </div>
  </div>

  <!-- Flat front cover, large -->
  <div class="cover cover--navy cover--hero" style="--w:320px; left:575px; top:150px;">
    <div class="cover__scene" role="img" aria-label="Night sky over a dark blue sea with a lone sailing boat silhouette"></div>
    <div class="cover__moon" role="img" aria-label="Full moon illustration with a warm glow"></div>
    <p class="cover__author">Maren Holloway</p>
    <h1 class="cover__title"><span>Harbours</span><span>Beneath</span><span>Quiet Skies</span></h1>
    <p class="cover__subtitle"><span>Drifting</span><span>Alone</span><span>Past</span><span>Amber</span><span>Straits</span></p>
  </div>
</section>

<section class="sheet"></section>

<p class="label label--back">BACK</p>

<div class="cover cover--slate" style="--w:230px; left:140px; top:808px;">
  <div class="cover__scene" role="img" aria-label="Night sky fading into a dark blue sea"></div>
  <h3 class="back__heading">About the author</h3>
  <div class="back__portrait" role="img" aria-label="Round portrait photo of the author"></div>
  <div class="back__body">
    <p class="narrow">Maren has spent most of her adult life at sea, sailing small boats alone across open water. She writes at night by lantern light, keeping notes on weather, tide and memory, and shaping them later into the poems gathered here.</p>
    <p class="narrow">Her work moves between fear and wonder, between long calms and sudden squalls. It is honest, sometimes raw, and always rooted in the quiet discipline of keeping watch through the dark hours until the first grey light.</p>
    <p>This is the second book in a series of five collections written over many passages. Each one follows a different stretch of water and a different season of the heart, yet all share the same moon, the same stars and the same small boat.</p>
  </div>
  <div class="back__code-area"></div>
</div>

<p class="label label--extra">2 EXAMPLES OF ADDITIONAL COVERS</p>

<div class="cover cover--dusk" style="--w:228px; left:646px; top:808px;">
  <div class="cover__scene" role="img" aria-label="Dusky night sky over a dark blue sea with a lone sailing boat silhouette"></div>
  <div class="cover__moon" role="img" aria-label="Full moon illustration with a warm glow"></div>
  <p class="cover__author">Maren Holloway</p>
  <h2 class="cover__title"><span>Harbours</span><span>Beneath</span><span>Quiet Skies</span></h2>
  <p class="cover__subtitle"><span>Drifting</span><span>Alone</span><span>Past</span><span>Ember</span><span>Bays</span></p>
</div>

<div class="cover cover--slate" style="--w:227px; left:845px; top:789px;">
  <div class="cover__scene" role="img" aria-label="Dark grey night sky over a blue sea with a lone sailing boat silhouette"></div>
  <div class="cover__moon" role="img" aria-label="Full moon illustration with a soft glow"></div>
  <p class="cover__author">Maren Holloway</p>
  <h2 class="cover__title"><span>Harbours</span><span>Beneath</span><span>Quiet Skies</span></h2>
  <p class="cover__subtitle"><span>Drifting</span><span>Alone</span><span>Past</span><span>Ember</span><span>Bays</span></p>
</div>

</body>
</html>
```